Corporate web site design for a blockchain oriented company

Design a web site for Tessaro. The company works on blockchain projects, mostly in B2B . Logo and content of the web site are attached with the project.

Corporate web sites means that we need to present the company and, at least, two of its projects.

Target Market(s)

B2B (Telecom, Gvt, online e-commerce web sites, banks, insurance ...)

Number of Pages Required

3 page

Font styles to use
Sans Serif

Requirements
Must have
• Landing page
• Page for KYC product
• Page for Loyalty product
• Team presentation
• Contact form
• Company presentation
• Several section can be in one page.
Nice to have
• Teaser video per project.
Should not have
• Heavy web site with a lot of animations.

```html
<!DOCTYPE html>
<html lang="en">
<head>
<meta charset="utf-8">
<title>Tessaro Technology</title>
<link href="https://fonts.googleapis.com/css2?family=Roboto:wght@300;400;500;700&display=swap" rel="stylesheet">
<style>
  :root {
    --gold: #cdb24c;
    --gold-text: #d1b149;
    --white: #ffffff;
    --ink: #1c1c1c;
    --panel: #efeff1;
    --hero-dark: #4a4540;
    --hero-mid: #8c8379;
  }
  * { box-sizing: border-box; margin: 0; padding: 0; }
  html, body { width: 1200px; height: 2494px; overflow: hidden; }
  body {
    position: relative;
    background: var(--white);
    font-family: "Roboto", Arial, sans-serif;
    color: var(--ink);
  }

  .top-bar {
    height: 51px;
    background: var(--gold);
    color: var(--white);
    font-size: 25px;
    font-weight: 300;
    text-align: right;
    padding: 8px 20px 0 0;
  }

  .site-header {
    height: 103px;
    display: flex;
    align-items: center;
    justify-content: space-between;
    padding: 0 58px 0 60px;
  }
  .brand-name {
    font-size: 40px;
    font-weight: 400;
    letter-spacing: 5px;
    color: var(--ink);
  }
  .main-nav { display: flex; gap: 18px; }
  .main-nav a {
    font-size: 33px;
    font-weight: 400;
    color: var(--ink);
    text-decoration: none;
  }

  .hero {
    position: relative;
    height: 477px;
    background:
      linear-gradient(rgba(40,36,32,0.45), rgba(40,36,32,0.45)),
      radial-gradient(ellipse at 30% 40%, #b9b2a6 0%, var(--hero-mid) 40%, var(--hero-dark) 100%);
    display: flex;
    align-items: center;
    justify-content: center;
  }
  .hero-title {
    font-size: 54px;
    font-weight: 400;
    line-height: 1.2;
    color: var(--white);
    text-align: center;
    margin-top: -34px;
  }

  .mission-band {
    height: 123px;
    background: var(--gold);
    color: var(--white);
    font-size: 25px;
    font-weight: 300;
    line-height: 39px;
    text-align: center;
    padding: 22px 120px 0;
  }
  .mission-band strong { font-weight: 700; }

  .feature-row {
    display: flex;
    height: 479px;
  }
  .feature-row.tall { height: 478px; }
  .feature-media, .feature-text { width: 600px; height: 100%; }
  .feature-text {
    background: var(--panel);
    padding-top: 70px;
  }
  .feature-heading {
    font-size: 27px;
    font-weight: 500;
    color: var(--gold-text);
    padding-bottom: 12px;
    border-bottom: 2px solid var(--gold-text);
    width: 210px;
    white-space: nowrap;
    margin-bottom: 28px;
  }
  .feature-body {
    font-size: 25px;
    font-weight: 300;
    line-height: 32px;
    color: var(--ink);
  }
  .contact-button {
    display: inline-block;
    margin-top: 34px;
    width: 192px;
    height: 43px;
    line-height: 43px;
    background: var(--gold);
    color: var(--white);
    font-size: 27px;
    font-weight: 500;
    text-align: center;
    text-decoration: none;
  }

  .why .feature-text { padding-left: 69px; padding-right: 70px; padding-top: 80px; }
  .what .feature-text { padding-left: 55px; padding-right: 75px; padding-top: 90px; }
  .how .feature-text { padding-left: 684px; }
  .how .feature-text { padding-left: 84px; padding-right: 52px; padding-top: 90px; }

  .media-globe {
    background: radial-gradient(circle at 52% 68%, #5f8fb0 0%, #2f5878 32%, #1b1f26 60%),
                linear-gradient(135deg, #6b3a1e, #161616);
    background-blend-mode: screen;
  }
  .media-laptop {
    background: radial-gradient(ellipse at 55% 45%, #d8d8da 0%, #bfbfc2 22%, #6b4a33 40%, #3c2a1f 100%);
  }
  .media-handshake {
    background: linear-gradient(160deg, #2f3338 0%, #7c8791 35%, #d9dadb 60%, #8a7e72 100%);
  }

  .site-footer {
    position: absolute;
    left: 0; top: 2189px;
    width: 1200px; height: 305px;
    background: var(--gold);
    color: var(--white);
  }
  .footer-col {
    position: absolute;
    top: 67px;
    text-align: center;
    font-size: 28px;
    font-weight: 300;
    line-height: 38px;
  }
  .footer-col h3 { font-size: 30px; font-weight: 500; line-height: 38px; }
  .footer-contact { left: 166px; width: 200px; }
  .footer-find { left: 500px; width: 200px; }
  .footer-map { left: 854px; font-size: 28px; font-weight: 300; text-align: left; }
  .social-links {
    position: absolute;
    left: 854px; top: 2436px;
    display: flex; gap: 16px;
  }
  .social-links span {
    display: block;
    width: 38px; height: 38px;
    background: var(--white);
    border-radius: 4px;
  }
</style>
</head>
<body>
  <div class="top-bar">Number</div>

  <header class="site-header">
    <div class="brand-name">TESSARO</div>
    <nav class="main-nav">
      <a href="#">Home</a>
      <a href="#">About</a>
      <a href="#">KYC</a>
      <a href="#">Loyalty</a>
      <a href="#">Contact</a>
    </nav>
  </header>

  <section class="hero" role="img" aria-label="Overhead view of a team table with laptops, phones and papers">
    <h1 class="hero-title">Tessaro<br>Technology</h1>
  </section>

  <div class="mission-band">
    Description: <strong>Blockchain solutions provider</strong> | Mission: Solving problems that<br>
    matter | Vision: Create a collaborative environment for all organisation
  </div>

  <section class="feature-row why">
    <div class="feature-media media-globe" role="img" aria-label="Close-up of a desk globe in warm light"></div>
    <div class="feature-text">
      <h2 class="feature-heading">Why Tessaro?</h2>
      <p class="feature-body">Tessaro Technology is a technology enabler that pledges to tackle issues that have plagued organisations for years. The company is lead by a team with tremendous expertise in the field of blockchain, mobile, IT, payment and financial sector. Being a global team, the company has influence in Singapore, China , France and more.</p>
    </div>
  </section>

  <section class="feature-row what">
    <div class="feature-text">
      <h2 class="feature-heading">What can Tessaro do?</h2>
      <p class="feature-body">Currently, Tessaro is solving business problems using blockchain technology. If you have an issue that you would like to enquire, we would love to hear from you!</p>
      <a class="contact-button" href="#">CONTACT</a>
    </div>
    <div class="feature-media media-laptop" role="img" aria-label="Hands typing on a laptop on a wooden table"></div>
  </section>

  <section class="feature-row tall how">
    <div class="feature-media media-handshake" role="img" aria-label="Two colleagues shaking hands over an office desk"></div>
    <div class="feature-text">
      <h2 class="feature-heading">How can Tessaro help?</h2>
      <p class="feature-body">Tessaro technology leverages on the most advanced blockchain technology that might not be available a few years ago. If you are not sure if we can help you, you can contact us here!</p>
      <a class="contact-button" href="#">CONTACT</a>
    </div>
  </section>

  <footer class="site-footer">
    <div class="footer-col footer-contact">
      <h3>Contact</h3>
      <p>Tel. ********</p>
      <p>Email. ********</p>
    </div>
    <div class="footer-col footer-find">
      <h3>Find us</h3>
      <p>Address</p>
    </div>
    <div class="footer-col footer-map">MAP</div>
  </footer>
  <div class="social-links" aria-label="Social links">
    <span></span><span></span><span></span><span></span>
  </div>
</body>
</html>
```